Brightwell Careers Homepage Redesign

Redevelopment work is underway on the Brightwell Careers website www.brightwell-careers.com - one task is to create a more compelling vertically stacked, mobile friendly homepage. The developers are not graphic designers and have been unable to produce an effective enough design. Their latest iteration can be seen @ http://novaquill.co.uk/brightwell_careers/index_5.html

The goal of the current design job is to:

a) produce a homepage design - reworking the attached draft concepts/designs to produce an effective landing page that will entice visitors to respond to the key call to action - to book a meeting with me to discuss their needs
b) ensure the design is aesthetically/functionally aligned with the rest of the site
c) ensure the design supports responsive implementation for viewing on a full range of desktop browsers and mobile devices.

Final output should be in a .psd file with all layers unmerged.

Further details on uploaded docs.

```html
<!DOCTYPE html>
<html lang="en">
<head>
<meta charset="utf-8">
<title>Brightwell Careers – Online Leadership Coaching &amp; Assessment</title>
<link href="https://fonts.googleapis.com/css2?family=Open+Sans:wght@400;600;700&family=Raleway:wght@400;600;700&display=swap" rel="stylesheet">
<style>
:root{
  --page:#e6e6e6;
  --navy:#17375e;
  --navy-deep:#0f2c4f;
  --blue:#2d5686;
  --blue-light:#2f5c8c;
  --orange:#f0901e;
  --orange-dark:#d9730c;
  --ink:#333;
  --muted:#666;
  --line:#bdbdbd;
  --wood:#2b2b2b;
}
*{box-sizing:border-box;margin:0;padding:0}
html,body{width:1200px;height:2376px;overflow:hidden}
body{position:relative;background:var(--page);font-family:"Open Sans",Arial,sans-serif;color:var(--ink)}
.abs{position:absolute}

/* header */
.brand{left:0;width:1200px;top:48px;text-align:center}
.brand-name{font-family:"Raleway",sans-serif;font-weight:700;font-size:34px;color:var(--navy);display:inline-flex;align-items:center;gap:12px}
.brand-name .dot{width:30px;height:30px;border-radius:50%;background:var(--orange)}
.brand-tag{font-size:13px;color:var(--muted);margin-top:6px}
.account-btn{top:22px;height:34px;border-radius:4px;color:#fff;font-size:9px;line-height:1.2;padding:7px 10px 0 30px}
.account-btn b{display:block;font-size:9px}
.account-btn small{font-size:7px}
.account-btn svg{position:absolute;left:10px;top:10px}
.login{left:838px;width:128px;background:var(--navy)}
.register{left:975px;width:125px;background:#111}
.register small{color:#e33}
.nav{left:0;width:1200px;top:165px;height:56px;border-top:1px solid var(--line);border-bottom:1px solid var(--line);display:flex;justify-content:center;align-items:center;gap:0;font-size:16px;font-weight:600;letter-spacing:.5px}
.nav span{padding:0 24px;border-left:2px solid #333;line-height:16px}
.nav span:first-child{border:0;color:var(--orange)}

/* slider */
.slider{left:0;top:221px;width:1200px;height:466px;background:linear-gradient(90deg,#2a2a2a,#3a3a3a 20%,#262626 45%,#383838 70%,#272727)}
.slider-rule{left:0;top:686px;width:1200px;height:12px;background:linear-gradient(var(--orange),var(--orange-dark))}
.side-slide{top:286px;width:205px;height:230px}
.slide-left{left:97px;background:radial-gradient(circle at 50% 50%,#ffffff 20%,#3aa0d8 60%,#2b8cc8)}
.slide-right{left:897px;background:linear-gradient(#8fb0cf,#6f8f6a 55%,#3f5f3c)}
.main-slide{left:303px;top:256px;width:594px;height:330px;background:linear-gradient(120deg,#2aa3c8,#1d8fb3 50%,#1a7ea3);box-shadow:0 4px 14px rgba(0,0,0,.5)}
.main-slide .photo{position:absolute;right:0;top:0;width:300px;height:330px;background:linear-gradient(90deg,rgba(255,255,255,.1),#5a6f86)}
.slide-copy{position:absolute;left:18px;top:18px;width:290px;color:#fff;text-align:center;font-size:28px;line-height:38px}
.slide-copy b{font-weight:700}
.book-chip{display:inline-block;margin:10px 0 14px;background:#173f6a;font-size:10px;line-height:12px;padding:4px 8px;text-align:left}
.slide-sub{font-size:25px;line-height:33px}
.slide-sub b{font-weight:700}
.caption{color:#fff;text-align:center}
.caption h4{font-weight:400;font-size:16px}
.caption p{font-size:10px;margin-top:6px}
.arrow{top:432px;width:52px;height:52px;border-radius:50%;background:#ddd}
.dots{top:674px;left:935px;display:flex;gap:6px}
.dots i{width:52px;height:5px;background:#ddd;border-radius:3px}
.dots i.on{background:var(--orange)}

/* leader panel */
.leader{left:98px;top:726px;width:1004px;height:384px;background:linear-gradient(#fff,#ececec);border:2px solid #ccc;overflow:hidden}
.boost{left:30px;top:56px;width:140px;height:140px;border-radius:50%;background:radial-gradient(#4a4a4a,#1a1a1a);border:5px solid #ddd;color:var(--orange);font-family:"Raleway",sans-serif;font-weight:700;font-size:17px;text-align:center;padding-top:44px}
.book-disc{left:780px;top:280px;width:220px;height:220px;border-radius:50%;background:radial-gradient(#2e4e70,#10243b);border:5px solid #ddd;color:var(--orange);font-size:17px;padding:52px 0 0 72px}
.headline{left:360px;top:78px;font-family:"Raleway",sans-serif;font-size:37px;line-height:46px;color:#555}
.headline strong{display:block;font-weight:700;color:var(--navy)}
.headline em{font-style:normal;color:var(--orange)}
.read-more{left:634px;top:188px;width:144px;height:40px;background:var(--orange);border:2px solid var(--orange-dark);border-radius:3px;font-size:14px;line-height:36px;text-align:center;color:#222}
.scroll-btn{left:938px;width:44px;height:38px;background:var(--blue)}
.list-box{left:18px;top:262px;width:412px;height:106px;border:1px solid #ccc;background:#fafafa;padding:10px 12px;font-size:12px;color:#555;display:grid;grid-template-columns:150px 100px 120px;row-gap:1px}
.list-box span::before{content:"➞ ";color:var(--orange)}
.list-box .wide{grid-column:1/4}

/* board + newsletter */
.band{left:0;top:1138px;width:1200px;height:162px;background:var(--navy)}
.person-icon{left:130px;top:1186px;width:60px;height:60px;border-radius:50%;background:#1b1b1b}
.quote{left:215px;top:1170px;width:380px;color:#fff}
.quote h3{font-size:15px;font-weight:700;letter-spacing:1px;line-height:20px}
.quote p{font-size:12px;margin-top:10px;line-height:19px}
.quote p i{font-size:11px}
.news{left:648px;top:1185px;color:#fff;font-size:16px;font-weight:700;letter-spacing:.5px}
.email{left:648px;top:1230px;width:325px;height:32px;border-radius:16px;background:#fff;font-size:10px;color:#888;font-style:italic;padding:9px 14px}
.subscribe{left:980px;top:1230px;width:104px;height:32px;border-radius:16px;background:#1d1d1d;color:#fff;font-size:11px;font-weight:700;text-align:center;line-height:32px}

/* staff */
.section-title{left:0;width:1200px;top:1308px;text-align:center;font-size:35px;color:#222}
.title-rule{left:455px;top:1362px;width:295px;height:2px;background:#888}
.title-rule::after{content:"";position:absolute;left:90px;top:-1px;width:115px;height:4px;background:var(--orange)}
.card{top:1404px;width:322px;height:474px;background:#ececec;border:1px solid #ccc}
.card .photo{height:224px;background:linear-gradient(#9aa7b6,#4c5868);position:relative}
.card .label{position:absolute;bottom:0;left:0;right:0;height:44px;background:rgba(0,0,0,.6);color:#fff;font-size:19px;letter-spacing:.5px;text-align:center;line-height:44px}
.card p{padding:20px 12px 0;font-size:15px;line-height:23px;color:#555;height:124px}
.card .social{display:flex;gap:4px;margin:24px 0 0 12px}
.card .social i{width:20px;height:20px;border:1px solid #ccc;background:#f4f4f4}
.card .learn{position:absolute;bottom:0;left:0;right:0;height:52px;background:var(--blue);color:#fff;text-align:center;line-height:52px;font-size:19px}

/* events */
.events{left:0;top:1916px;width:1200px;height:104px;background:var(--navy-deep)}
.events-rule{left:0;top:2020px;width:1200px;height:10px;background:var(--orange)}
.events-title{left:125px;top:1954px;font-family:"Raleway",sans-serif;font-size:26px;font-weight:700;color:var(--orange)}
.events-title b{color:#f4b531}
.date{top:1924px;width:86px;height:86px;border-radius:50%;background:#1e1e1e;color:#fff;text-align:center;padding-top:18px}
.date b{display:block;font-size:28px;line-height:30px}
.date small{font-size:11px}
.date.active{background:#2e5e8e}

/* footer */
.foot-h{top:2045px;font-size:17px;color:#222;letter-spacing:.5px}
.foot-circle{top:2078px;width:36px;height:36px;border-radius:50%;background:var(--navy)}
.blog{left:102px;top:2188px;width:310px;font-family:Georgia,serif;font-size:12px;color:#333}
.blog .t{font-size:14px}
.blog .d{font-size:8px;color:#888;margin:6px 0 4px}
.blog p{line-height:17px}
.blog .more{margin-top:12px}
.adv{left:455px;top:2074px;list-style:none;font-size:13px;line-height:25px;color:#444}
.adv li::before{content:"» ";color:#888}
.field{left:836px;width:264px;background:#8f8f8f;color:#ddd;font-family:Georgia,serif;font-size:11px;padding:6px 8px}
.submit{left:1030px;top:2286px;width:72px;height:30px;background:var(--orange);border:1px solid #c36b0c;text-align:center;line-height:28px;font-size:11px}
.foot-rule{left:0;top:2356px;width:1200px;height:20px;background:linear-gradient(var(--orange),var(--orange-dark))}
</style>
</head>
<body>

<header>
  <div class="abs brand">
    <div class="brand-name"><span class="dot"></span>Brightwell Careers</div>
    <div class="brand-tag">Online Leadership Coaching &amp; Assessment</div>
  </div>
  <div class="abs account-btn login">
    <svg width="12" height="14" viewBox="0 0 12 14"><rect x="1" y="6" width="10" height="8" fill="#fff"/><path d="M3 6V4a3 3 0 0 1 6 0v2" stroke="#fff" stroke-width="2" fill="none"/></svg>
    <b>CLIENT LOGIN</b><small>Create new account</small>
  </div>
  <div class="abs account-btn register">
    <svg width="12" height="14" viewBox="0 0 12 14"><rect x="1" y="6" width="10" height="8" fill="#fff"/><path d="M3 6V4a3 3 0 0 1 6 0v2" stroke="#fff" stroke-width="2" fill="none"/></svg>
    <b>REGISTER NOW</b><small>New users sign here</small>
  </div>
  <nav class="abs nav">
    <span>Transforming Leadership</span><span>Assesments</span><span>Coaching</span><span>Resources &amp; Tools</span><span>Bookings &amp; Prices</span>
  </nav>
</header>

<section>
  <div class="abs slider"></div>
  <div class="abs side-slide slide-left" role="img" aria-label="Banner 3 illustration: a businessperson at the centre of a connected network of people"></div>
  <div class="abs side-slide slide-right" role="img" aria-label="Banner 2 photo: river valley landscape with a strategy quote"></div>
  <div class="abs caption" style="left:97px;top:532px;width:205px"><h4>Banner 3</h4><p>Produced by Lumen Studios and released by Harborlight Pictures</p></div>
  <div class="abs caption" style="left:897px;top:532px;width:205px"><h4>Banner 2</h4><p>Produced by Lumen Studios and released by Harborlight Pictures</p></div>
  <div class="abs main-slide">
    <div class="photo" role="img" aria-label="Photo of a coach in a blue shirt and tie presenting"></div>
    <div class="slide-copy">
      Want to <b>motivate</b> your team to higher performance levels?
      <div><span class="book-chip">BOOK A<br>MEETING NOW</span></div>
      <div class="slide-sub">Brightwell Careers<br><b>Virtual Leadership Coaching</b><br>&amp; Assessment</div>
    </div>
  </div>
  <div class="abs caption" style="left:303px;top:605px;width:594px"><h4>Banner 1</h4><p style="font-size:14px">Produced by Lumen Studios and released by Harborlight Pictures</p></div>
  <div class="abs arrow" style="left:12px"><svg width="52" height="52"><path d="M30 16 20 26l10 10" stroke="#333" stroke-width="5" fill="none"/></svg></div>
  <div class="abs arrow" style="left:1136px"><svg width="52" height="52"><path d="M22 16l10 10-10 10" stroke="#333" stroke-width="5" fill="none"/></svg></div>
  <div class="abs dots"><i></i><i class="on"></i><i></i></div>
  <div class="abs slider-rule"></div>
</section>

<section class="abs leader">
  <svg class="abs" style="left:0;top:0" width="1004" height="384"><line x1="160" y1="170" x2="800" y2="320" stroke="#555" stroke-width="7"/></svg>
  <div class="abs boost" role="img" aria-label="Dashboard gauge photo">NEED A<br>BOOST?</div>
  <div class="abs book-disc" role="img" aria-label="Keyboard key photo">BOOK<br>NOW</div>
  <div class="abs headline">YOU ARE THE LEADER<strong>YOUR PEOPLE <em>EXPECT YOU TO:</em></strong></div>
  <div class="abs read-more">READ MORE</div>
  <div class="abs scroll-btn" style="top:20px"><svg width="44" height="38"><path d="M14 24l8-8 8 8" stroke="#fff" stroke-width="2" fill="none"/></svg></div>
  <div class="abs scroll-btn" style="top:62px;background:#2a2a2a"><svg width="44" height="38"><path d="M14 15l8 8 8-8" stroke="#fff" stroke-width="2" fill="none"/></svg></div>
  <div class="abs list-box">
    <span>Engage them</span><span>Develop them</span><span>Create culture</span>
    <span>Inspire them</span><span>Set vision</span><span>Resolve conflicts</span>
    <span>Motivate them</span><span>Define values</span><span>Solve problems</span>
    <span class="wide">Choose winning strategies</span>
    <span class="wide">Take care of business as usual</span>
  </div>
</section>

<section>
  <div class="abs band"></div>
  <div class="abs person-icon"><svg width="60" height="60"><circle cx="30" cy="24" r="7" fill="#fff"/><path d="M17 42a13 10 0 0 1 26 0z" fill="#fff"/></svg></div>
  <div class="abs quote">
    <h3>BOARD OF DIRECTORS<br>( NORTHFIELD SYSTEMS INC. )</h3>
    <p>" Ede semper est, vitae luctus metus libero eu augue. Morb sipo ipiscing, commodo quis, gravida ..." - <i>Kohn Doe / company name</i></p>
  </div>
  <div class="abs news">NEWS LETTER</div>
  <div class="abs email">enter your email id here ...</div>
  <div class="abs subscribe">SUBSCRIBE</div>
</section>

<section>
  <h2 class="abs section-title" style="font-weight:400">Our Staff</h2>
  <div class="abs title-rule"></div>
  <article class="abs card" style="left:100px">
    <div class="photo" role="img" aria-label="Portrait of an organisational leader"><div class="label">Organisational Leaders</div></div>
    <p>Lorem ipsum dolor situradipiscing elit. In mollis eramati nequilisisit amet ultricies erat rutrum. Cras facilisis, nulla vel viverra auceo . . . .</p>
    <div class="social"><i></i><i></i><i></i></div>
    <div class="learn">Learn More</div>
  </article>
  <article class="abs card" style="left:439px">
    <div class="photo" role="img" aria-label="Portrait of an HR and OD manager"><div class="label">HR &amp; OD Managers</div></div>
    <p>Lorem ipsum dolor situradipiscing elit. In mollis eramati nequilisisit amet ultricies erat rutrum. Cras facilisis, nulla vel viverra auceo . . . .</p>
    <div class="social"><i></i><i></i><i></i></div>
    <div class="learn">Learn More</div>
  </article>
  <article class="abs card" style="left:778px">
    <div class="photo" role="img" aria-label="Portrait of a team leader"><div class="label">Team Leaders</div></div>
    <p>Lorem ipsum dolor situradipiscing elit. In mollis eramati nequilisisit amet ultricies erat rutrum. Cras facilisis, nulla vel viverra auceo . . . .</p>
    <div class="social"><i></i><i></i><i></i></div>
    <div class="learn">Learn More</div>
  </article>
</section>

<section>
  <div class="abs events"></div>
  <div class="abs events-title">UPCOMMING <b>EVENTS</b></div>
  <div class="abs date" style="left:442px"><b>12</b><small>SEP</small></div>
  <div class="abs date active" style="left:580px"><b>17</b><small>SEP</small></div>
  <div class="abs date" style="left:707px"><b>20</b><small>SEP</small></div>
  <div class="abs date" style="left:833px"><b>25</b><small>SEP</small></div>
  <div class="abs date" style="left:980px"><b>30</b><small>SEP</small></div>
  <div class="abs events-rule"></div>
</section>

<footer>
  <h3 class="abs foot-h" style="left:102px;font-weight:400">SOCIAL LINKS</h3>
  <div class="abs foot-circle" style="left:102px"></div>
  <div class="abs foot-circle" style="left:150px;background:#4a5a6a"></div>
  <div class="abs foot-circle" style="left:198px;background:#555"></div>
  <h3 class="abs foot-h" style="left:102px;top:2155px;font-weight:400">BLOGS</h3>
  <div class="abs blog">
    <div class="t">Post Title</div>
    <div class="d">Friday, 8th August 2014</div>
    <p>Lorem ipsum dolor sit amet, consectetur adipiscing elit. Nunc non diam erat. In fringilla massa ut nisi ullamcorper pellentesque.</p>
    <div class="more">Read More »</div>
  </div>
  <h3 class="abs foot-h" style="left:455px;font-weight:400">ADVERTISE WITH US</h3>
  <ul class="abs adv">
    <li>Lorem ipsum dolor sit</li><li>Amet consectetur</li><li>Praesent vel sem id</li><li>Curabitur hendrerit est</li><li>Aliquam eget erat nec sapien</li><li>Cras id augue nunc</li><li>In nec justo non</li><li>Vivamus mollis enim ut</li><li>Curabitur hendrerit est</li>
  </ul>
  <h3 class="abs foot-h" style="left:836px;font-weight:400">CONTACT US</h3>
  <div class="abs field" style="top:2072px;height:28px">Name</div>
  <div class="abs field" style="top:2108px;height:28px">Email</div>
  <div class="abs field" style="top:2144px;height:118px">Massage</div>
  <div class="abs submit">SUBMIT</div>
  <div class="abs foot-rule"></div>
</footer>

</body>
</html>
```